Master & Realtor Did you know

I am a realtor and also a Master in Korean Martial arts, I would like to specifically market to my Karate clientele and make them aware that I am a realtor for the last 12 years in addition to being a karate instructor. also the similarities between both jobs Integrity, perseverance ,dedication, etc... also I would like to use a photo of myself on the front of the postcard that shows me in uniform and my suite attire.or I am open to a different approachRobert Reynolds

Target Market(s)

MY Karate clients

Industry/Entity Type

Real Estate Agent

Requirements
Must have
• Bullet points on the back with description of both job similarities example..
• Integrity, perseverance, focus, determination , people skills, be able to finish what I have started with the anticipated outcome.
• 33 years in teaching Martial Arts, 12 years as a professional Realtor.
• Please feel free to use your own words in description

```html
<!DOCTYPE html>
<html lang="en">
<head>
<meta charset="utf-8">
<title>Master &amp; Realtor Postcard</title>
<link href="https://fonts.googleapis.com/css2?family=Montserrat:wght@700;800&family=Lato:ital,wght@0,400;0,700;1,400;1,700;1,900&display=swap" rel="stylesheet">
<style>
  :root {
    --navy: #0e1a3c;
    --blue: #1aa7ee;
    --ink: #1b1b1b;
    --white: #ffffff;
    --backdrop: #e6e7e9;
    --line: #b9b9b9;
  }
  * { box-sizing: border-box; margin: 0; padding: 0; }
  html, body { width: 902px; height: 1200px; overflow: hidden; background: var(--backdrop); }
  body { position: relative; font-family: "Lato", sans-serif; color: var(--ink); }

  .card {
    position: absolute;
    left: 121px;
    width: 660px;
    height: 512px;
    background: var(--white);
    overflow: hidden;
    box-shadow: 0 2px 8px rgba(0,0,0,.18);
  }
  .card--front { top: 44px; }
  .card--back  { top: 640px; }
  .card__shapes { position: absolute; inset: 0; }
  .abs { position: absolute; }

  /* Front */
  .brand-karate { left: 10px; top: 12px; width: 70px; text-align: center; }
  .brand-karate__dot { width: 30px; height: 30px; border-radius: 50%; background: var(--navy); margin: 0 auto 4px; }
  .brand-karate__name { font-family: "Montserrat", sans-serif; font-weight: 700; font-size: 9px; color: var(--navy); line-height: 1.15; }

  .photo--uniform { left: 70px; top: 14px; width: 170px; height: 250px; background: linear-gradient(180deg, #f1f1f1 0%, #2a2a2e 45%, #141416 100%); }

  .headline { right: 20px; top: 30px; text-align: right; }
  .headline__title { font-family: "Montserrat", sans-serif; font-weight: 800; font-size: 39px; letter-spacing: .3px; color: var(--ink); line-height: 1; }
  .headline__question { font-family: "Lato", sans-serif; font-weight: 700; font-size: 58px; color: var(--blue); line-height: 1.05; margin-top: 4px; }
  .headline__note { font-style: italic; font-weight: 700; font-size: 17px; line-height: 1.35; margin-top: 10px; }

  .brand-realty { left: 18px; top: 288px; display: flex; align-items: center; gap: 8px; }
  .brand-realty__mark { width: 14px; height: 14px; background: var(--ink); }
  .brand-realty__name { font-size: 17px; line-height: 1.1; color: var(--ink); }

  .intro { left: 24px; top: 342px; width: 380px; }
  .intro__lead { font-weight: 700; font-size: 14.5px; }
  .intro__years { font-style: italic; font-weight: 700; font-size: 20px; color: var(--blue); line-height: 1.3; margin-top: 6px; }

  .call { font-family: "Montserrat", sans-serif; font-weight: 700; }
  .call--front { left: 30px; top: 446px; font-size: 33px; color: var(--white); }
  .call__label { color: var(--blue); }

  .portrait { left: 420px; top: 206px; width: 232px; height: 232px; border-radius: 50%; background: radial-gradient(circle at 50% 40%, #c9ccd0 0%, #a8abb0 55%, #2b2d33 100%); }

  /* Back */
  .photo--training { left: 0; top: 0; width: 166px; height: 170px; background: linear-gradient(135deg, #cfd3d8, #6c7280); }
  .photo--house { left: 166px; top: 0; width: 220px; height: 170px; background: linear-gradient(180deg, #7fb6e6 0%, #9b6a4a 45%, #4d6e36 100%); }

  .tag { left: 10px; top: 195px; background: var(--blue); color: var(--white); font-family: "Montserrat", sans-serif; font-weight: 700; font-size: 12.5px; padding: 3px 14px 3px 10px; border-radius: 0 12px 12px 0; }
  .similar { left: 18px; top: 228px; width: 290px; color: var(--white); }
  .similar__lead { font-style: italic; font-weight: 700; font-size: 12px; line-height: 1.25; }
  .similar__list { list-style: none; margin-top: 8px; }
  .similar__list li { position: relative; padding-left: 16px; font-size: 10px; line-height: 1.3; margin-bottom: 5px; }
  .similar__list li::before { content: ""; position: absolute; left: 1px; top: 4px; width: 6px; height: 6px; border-radius: 50%; background: var(--blue); }

  .call-bar { left: 0; top: 380px; width: 320px; height: 46px; background: var(--blue); }
  .call--back { left: 20px; top: 389px; font-size: 22px; color: var(--white); }
  .call--back .call__label { color: var(--navy); }

  .stamp { left: 498px; top: 53px; width: 68px; height: 68px; border: 1.5px solid var(--ink); }
  .address-line { left: 337px; width: 252px; height: 2px; background: var(--line); }
  .address-line--1 { top: 243px; }
  .address-line--2 { top: 270px; }
  .address-line--3 { top: 297px; }
</style>
</head>
<body>

<section class="card card--front">
  <div class="abs photo--uniform" role="img" aria-label="Photo of the instructor in his martial arts uniform"></div>

  <svg class="card__shapes" viewBox="0 0 660 512" aria-hidden="true">
    <path d="M0 190 Q 280 300 660 200 L660 512 L0 512 Z" fill="#0e1a3c"/>
    <path d="M0 206 Q 280 312 660 214 L660 512 L0 512 Z" fill="#1aa7ee"/>
    <path d="M0 212 Q 280 320 660 222 L660 512 L0 512 Z" fill="#ffffff"/>
    <path d="M0 380 L660 380 L660 512 L0 512 Z" fill="#0e1a3c"/>
    <path d="M0 240 Q 260 320 430 300 L430 400 Q 420 418 400 418 L0 418 Z" fill="#ffffff"/>
    <circle cx="536" cy="322" r="128" fill="#0e1a3c"/>
    <circle cx="536" cy="322" r="122" fill="#1aa7ee"/>
    <circle cx="536" cy="322" r="118" fill="#ffffff"/>
  </svg>

  <div class="abs brand-karate">
    <div class="brand-karate__dot"></div>
    <div class="brand-karate__name">STONE RIVER KARATE</div>
  </div>

  <div class="abs headline">
    <h1 class="headline__title">MASTER &amp; REALTOR</h1>
    <p class="headline__question">Did you know?</p>
    <p class="headline__note">There are many similarities between both jobs<br>Integrity, perseverance ,dedication, etc...</p>
  </div>

  <div class="abs brand-realty">
    <span class="brand-realty__mark"></span>
    <span class="brand-realty__name">Harlow Pines Real Estate</span>
  </div>

  <div class="abs intro">
    <p class="intro__lead">I am a realtor and also a Master in Korean Martial arts</p>
    <p class="intro__years">33 years in teaching Martial Arts and<br>12 years as a professional Realtor</p>
  </div>

  <p class="abs call call--front"><span class="call__label">Call me:</span> 0123456789</p>

  <div class="abs portrait" role="img" aria-label="Portrait photo of the realtor in a suit"></div>
</section>

<section class="card card--back">
  <div class="abs photo--training" role="img" aria-label="Photo of a martial arts sparring session"></div>
  <div class="abs photo--house" role="img" aria-label="Photo of a family house"></div>

  <svg class="card__shapes" viewBox="0 0 660 512" aria-hidden="true">
    <path d="M386 0 L660 0 L660 512 L0 512 L0 130 Q 60 175 200 170 Q 360 150 386 0 Z" fill="#ffffff"/>
    <path d="M0 130 Q 60 175 200 170 Q 360 150 386 0" fill="none" stroke="#1aa7ee" stroke-width="9"/>
    <path d="M0 150 Q 120 200 320 160 L320 380 L0 380 Z" fill="#0e1a3c"/>
    <path d="M0 150 Q 120 200 320 160" fill="none" stroke="#ffffff" stroke-width="6"/>
  </svg>

  <p class="abs tag">JOB SIMILARITIES</p>

  <div class="abs similar">
    <p class="similar__lead">Integrity, perseverance, focus, determination , people skills, be able to finish what I have started with the anticipated outcome.</p>
    <ul class="similar__list">
      <li>Lorem ipsum dolor sit amet, consectetuer adipiscing elit. Aenean commodo ligula eget dolor.</li>
      <li>Aenean massa. Cum sociis natoque penatibus et magnis dis parturient montes,</li>
      <li>Nascetur ridiculus mus. Donec quam felis, ultricies nec, pellentesque eu, pretium quis, sem.</li>
    </ul>
  </div>

  <div class="abs call-bar"></div>
  <p class="abs call call--back"><span class="call__label">Call me :</span> 0123456789</p>

  <div class="abs stamp"></div>
  <div class="abs address-line address-line--1"></div>
  <div class="abs address-line address-line--2"></div>
  <div class="abs address-line address-line--3"></div>
</section>

</body>
</html>
```